Very Simple/Minimal Business Card Design Project

The company operates in the industrial maritime infrastructure sector in Brazil. You can find more information on our website www.navortek.com.br WE NEED TO LOOK POWERFUL AND SERIOUS
I have attached a copy of the old cards. We would like something more professional / industrial / sexy that also includes the position.

The card can be double sided or not. We would like you to propose as many options.

Thank you
Updates

Many thanks, do let me know if you have any questions. I am under a lot of time pressure to try and have them printed over the next days or so.

Please could you use the following information

for the address: Rua Tapiraçu, 417 - Centro, Rio de Janeiro, 20034-118, Brasil

for the mobile: +55 21 8237 9412
for the landline: +55 21 4096 3578

and position:  Diretor Geral

Thakn you

Target Market(s)

Shipowners, bankers, industrial companies

Industry/Entity Type

Industrial

Requirements
Must have
• POWERFUL
SERIOUS
SOLID
BIG CORPORATION

```html
<!DOCTYPE html>
<html lang="pt-BR">
<head>
<meta charset="utf-8">
<title>Navortek – Cartão de Visita</title>
<link rel="stylesheet" href="https://fonts.googleapis.com/css2?family=Open+Sans:wght@400;600;700&display=swap">
<style>
  :root {
    --navy: #2c3769;
    --green: #1f9a4e;
    --strip-grey: #e4e5e8;
    --paper: #ffffff;
    --ink-soft: #4a4f66;
    --stage: #d9dadd;
  }
  * { box-sizing: border-box; margin: 0; padding: 0; }
  html, body { width: 1200px; height: 899px; overflow: hidden; }
  body {
    background: var(--stage);
    font-family: "Open Sans", Arial, sans-serif;
    position: relative;
  }
  .card {
    position: absolute;
    top: 305px;
    width: 520px;
    height: 289px;
    overflow: hidden;
    box-shadow: 0 6px 18px rgba(0,0,0,.18);
  }
  .card--front { left: 50px; background: var(--paper); }
  .card--back { left: 630px; background: var(--navy); }

  .brand-name {
    font-weight: 600;
    color: var(--navy);
    line-height: 1;
    white-space: nowrap;
  }

  /* front */
  .brand-strip {
    position: absolute; left: 0; top: 0; bottom: 0; width: 70px;
    background: var(--strip-grey);
  }
  .brand-strip .brand-name {
    position: absolute; left: 35px; top: 150px;
    transform: translate(-50%, -50%) rotate(-90deg);
    font-size: 26px;
  }
  .edge-stripes {
    position: absolute; top: 0; bottom: 0; right: 0; width: 48px; background: var(--paper);
  }
  .edge-stripes .stripe-green { position: absolute; left: 0; top: 0; bottom: 0; width: 6px; background: var(--green); }
  .edge-stripes .stripe-navy { position: absolute; left: 6px; top: 0; bottom: 0; width: 9px; background: var(--navy); }
  .web-vertical {
    position: absolute; top: 50%;
    transform: translate(50%, -50%) rotate(-90deg);
    white-space: nowrap; font-size: 11px; letter-spacing: .3px;
  }
  .web-vertical--front { right: 16px; color: var(--navy); }
  .holder { position: absolute; left: 110px; top: 58px; }
  .holder-name { font-weight: 700; color: var(--navy); font-size: 17px; line-height: 1.2; }
  .holder-role { color: var(--ink-soft); font-size: 12px; }
  .contact { position: absolute; left: 98px; top: 172px; list-style: none; }
  .contact li {
    display: flex; align-items: flex-start; gap: 7px;
    font-size: 10.5px; color: var(--navy); line-height: 1.35; margin-bottom: 5px;
  }
  .contact svg { width: 12px; height: 12px; flex: none; margin-top: 1px; fill: var(--green); }
  .contact .label { display: inline-block; width: 48px; }

  /* back */
  .brand-band {
    position: absolute; left: 0; top: 116px; width: 295px; height: 70px;
    background: var(--paper);
    display: flex; align-items: center; justify-content: center;
  }
  .brand-band .brand-name { font-size: 34px; }
  .back-edge {
    position: absolute; top: 0; bottom: 0; right: 0; width: 44px; background: var(--paper);
  }
  .back-edge .stripe-green { position: absolute; left: 0; top: 0; bottom: 0; width: 5px; background: var(--green); }
  .web-vertical--back { right: 17px; color: var(--green); }
</style>
</head>
<body>

<section class="card card--front" aria-label="Frente do cartão">
  <div class="brand-strip">
    <span class="brand-name">Navortek</span>
  </div>

  <div class="holder">
    <p class="holder-name">Leonard Whitcombe</p>
    <p class="holder-role">Diretor Geral</p>
  </div>

  <ul class="contact">
    <li>
      <svg viewBox="0 0 12 12" aria-hidden="true"><path d="M6 1 L11.5 6 H10 V11 H7.3 V8 H4.7 V11 H2 V6 H0.5 Z"/></svg>
      <span>Rua Tapiraçu, 417 - Centro,<br>Rio de Janeiro, 20034-118, Brasil</span>
    </li>
    <li>
      <svg viewBox="0 0 12 12" aria-hidden="true"><path d="M2.5 1 L4.5 1 L5.3 3.6 L4 4.6 C4.7 6.1 5.9 7.3 7.4 8 L8.4 6.7 L11 7.5 L11 9.5 C11 10.4 10.3 11 9.4 11 C4.8 10.7 1.3 7.2 1 2.6 C1 1.7 1.6 1 2.5 1 Z"/></svg>
      <span><span class="label">landline:</span>+55 21 4096 3578<br><span class="label">mobile:</span>+55 21 8237 9412</span>
    </li>
    <li>
      <svg viewBox="0 0 12 12" aria-hidden="true"><path d="M0.5 2 H11.5 V10 H0.5 Z M1.5 3 V3.4 L6 6.6 L10.5 3.4 V3 Z M1.5 4.6 V9 H10.5 V4.6 L6 7.8 Z" fill-rule="evenodd"/></svg>
      <span>geral@navortek.com.br</span>
    </li>
  </ul>

  <div class="edge-stripes">
    <span class="stripe-green"></span>
    <span class="stripe-navy"></span>
  </div>
  <p class="web-vertical web-vertical--front">www.navortek.com.br</p>
</section>

<section class="card card--back" aria-label="Verso do cartão">
  <div class="brand-band">
    <span class="brand-name">Navortek</span>
  </div>
  <div class="back-edge">
    <span class="stripe-green"></span>
  </div>
  <p class="web-vertical web-vertical--back">www.navortek.com.br</p>
</section>

</body>
</html>
```